3 Politically Incorrect Greeting Cards

I would like to see some clean, colorful, and modern designs for 3 "politically incorrect" greeting cards aimed at young, single, successful women. I would like them to say:

Card 1: " Congratulations on not marrying the wrong person"
Card 2: " Congratulations on buying a house without a husband"
Card 3: " Thank you for not forgetting about me now that you have a boyfriend"

My initial thought was to have a white background with simple black writing, but I think a colorful background with a white text box in the middle might be more appropriate. I can't imagine the cards having any images/icons on them, but I'm open to suggestions if you think it would improve on the design. You guys are likely more creative than I am.

I've included a couple pics of looks I like - but like I said - I'm open to suggestions and what I like may not be appropriate for these cards. All the cards can have a similar esthetic or theme (maybe the same fonts but different colors or different color florals in each) or they can be completely different.

Target Market(s)

Young, single, successful women mid-20s to mid 40's.

Font styles to use
Serif
Sans Serif
Other font styles liked:
• Watercolour lettering maybe

Colors

Designer to choose colors to be used in the design.

Requirements
Must have
• Clean, colorful, bright, professional looking. The right tone for the message.
• I think the message is bold so the writing and colors have to be as well. I have included examples of ideas I like.
Nice to have
• Images, illustrations, icons, maybe patterns or some decorative details. Something to make the card more interesting than just the words (like the blue background with black letters one I made). I like a bright pattern with a white box in the center with the text.
Should not have
• Special effects, galaxy pictures, ugly images, bland colors.

```html
<!DOCTYPE html>
<html lang="en">
<head>
<meta charset="UTF-8">
<title>Greeting Card – Congratulations on not marrying the wrong person</title>
<link rel="stylesheet" href="https://fonts.googleapis.com/css2?family=Dancing+Script:wght@600&display=swap">
<style>
  :root {
    --backdrop-pink: #f9c5c8;
    --card-white: #ffffff;
    --hibiscus-pink: #f2a0ae;
    --coral: #f4b3a6;
    --palm-teal: #17706c;
    --fern-aqua: #8fd6dc;
    --orchid: #b65aa6;
    --ink-teal: #0f4a5a;
    --veil: rgba(255, 255, 255, 0.86);
  }

  * { margin: 0; padding: 0; box-sizing: border-box; }

  html, body {
    width: 1200px;
    height: 1200px;
    overflow: hidden;
  }

  body {
    background: var(--backdrop-pink);
    position: relative;
  }

  .card {
    position: absolute;
    left: 46px;
    top: 204px;
    width: 1112px;
    height: 784px;
    background: var(--card-white);
    overflow: hidden;
  }

  .card__pattern {
    position: absolute;
    inset: 0;
    background:
      radial-gradient(circle at 8% 10%, var(--fern-aqua) 0 8%, transparent 18%),
      radial-gradient(circle at 22% 4%, var(--palm-teal) 0 6%, transparent 14%),
      radial-gradient(circle at 50% 5%, var(--hibiscus-pink) 0 7%, transparent 15%),
      radial-gradient(circle at 80% 4%, var(--fern-aqua) 0 6%, transparent 14%),
      radial-gradient(circle at 95% 8%, var(--palm-teal) 0 7%, transparent 16%),
      radial-gradient(circle at 10% 35%, var(--hibiscus-pink) 0 9%, transparent 18%),
      radial-gradient(circle at 4% 62%, var(--fern-aqua) 0 6%, transparent 14%),
      radial-gradient(circle at 12% 85%, var(--coral) 0 8%, transparent 16%),
      radial-gradient(circle at 97% 40%, var(--palm-teal) 0 9%, transparent 18%),
      radial-gradient(circle at 94% 60%, var(--hibiscus-pink) 0 8%, transparent 16%),
      radial-gradient(circle at 92% 88%, var(--palm-teal) 0 8%, transparent 16%),
      radial-gradient(circle at 50% 96%, var(--hibiscus-pink) 0 7%, transparent 15%),
      radial-gradient(circle at 30% 97%, var(--fern-aqua) 0 6%, transparent 14%),
      radial-gradient(circle at 72% 96%, var(--fern-aqua) 0 6%, transparent 14%),
      linear-gradient(135deg, #fdeef2, #eaf7f7 50%, #f8e4ef);
  }

  .card__message-panel {
    position: absolute;
    left: 162px;
    top: 68px;
    width: 786px;
    height: 646px;
    background: var(--veil);
    display: flex;
    flex-direction: column;
    align-items: center;
    justify-content: center;
  }

  .card__message {
    font-family: "Dancing Script", cursive;
    font-weight: 600;
    font-size: 92px;
    line-height: 104px;
    color: var(--ink-teal);
    text-align: center;
    letter-spacing: -1px;
  }

  .card__message span { display: block; }
</style>
</head>
<body>
  <div class="card">
    <div class="card__pattern" role="img" aria-label="Watercolour tropical pattern of pink hibiscus flowers, teal palm leaves and aqua ferns framing the card"></div>
    <div class="card__message-panel">
      <p class="card__message">
        <span>Congratulations</span>
        <span>on not</span>
        <span>marrying</span>
        <span>the wrong</span>
        <span>person</span>
      </p>
    </div>
  </div>
</body>
</html>
```